Business Card Design

I would like a new business card design for an accounting firm that specializes in resolving clients tax problems. I want the card to give the impression that we are not your typical stodgy accounting firm, but at the same time we will get the job done.
Industry/Entity Type
Business
Contact Information for Business Card
Dorian T Welsby
Certified Public Accountant
38-27 52nd Street
Sunnyside, NY 11287
Tel: (718) 555-0142
Fax: (888) 555-0199
e-mail: dtwthecpa@ledgerpost.com
website: harborfilingreliefexperts.com

```html
<!DOCTYPE html>
<html lang="en">
<head>
<meta charset="utf-8">
<title>Dorian T Welsby – Business Card</title>
<link rel="stylesheet" href="https://fonts.googleapis.com/css2?family=Jost:wght@500&family=Tinos:wght@400;700&display=swap">
<style>
  :root {
    --card-bg: #141414;
    --accent: #fff200;
    --text-light: #ffffff;
    --key-grey: #404244;
    --key-dark: #111213;
    --key-border: #a2a2a2;
    --key-text: #ffffff;
  }
  html, body {
    margin: 0;
    padding: 0;
    width: 704px;
    height: 1200px;
    overflow: hidden;
    background: var(--card-bg);
  }
  .card {
    position: relative;
    width: 704px;
    height: 1200px;
    background: var(--card-bg);
    font-family: "Tinos", "Times New Roman", serif;
    color: var(--text-light);
  }
  .holder-name {
    position: absolute;
    left: 56px;
    top: 52px;
    margin: 0;
    font-family: "Jost", "Futura", sans-serif;
    font-weight: 500;
    font-size: 57px;
    line-height: 1;
    color: var(--accent);
    letter-spacing: 0.2px;
  }
  .holder-title {
    position: absolute;
    left: 150px;
    top: 124px;
    margin: 0;
    font-size: 23px;
    line-height: 1;
  }
  .contact {
    position: absolute;
    left: 81px;
    top: 338px;
    margin: 0;
    padding: 0;
    list-style: none;
  }
  .contact li { white-space: nowrap; }
  .contact .phone { font-size: 32px; line-height: 40px; }
  .contact .email,
  .contact .web { font-size: 26px; line-height: 36px; }
  .contact .address { font-size: 26px; line-height: 38px; color: var(--accent); }

  .keypad {
    position: absolute;
    left: 53px;
    top: 555px;
    width: 596px;
    display: grid;
    grid-template-columns: 140px 140px 140px 140px;
    grid-template-rows: 91px 91px 92px 92px 92px 99px;
    column-gap: 12px;
    row-gap: 13px;
  }
  .key {
    display: flex;
    align-items: center;
    justify-content: center;
    box-sizing: border-box;
    font-weight: 700;
    font-size: 31px;
    color: var(--key-text);
    background: var(--key-grey);
  }
  .key--digit {
    background: var(--key-dark);
    border: 2px solid var(--key-border);
  }
  .key--blank {
    background: var(--key-dark);
    border: 2px solid var(--key-border);
  }
  .key--equals {
    background: var(--accent);
    color: #000;
  }
</style>
</head>
<body>
  <div class="card">
    <h1 class="holder-name">Dorian T Welsby</h1>
    <p class="holder-title">Certified Public Accountant</p>

    <ul class="contact">
      <li class="phone">Tel : (718) 555-0142</li>
      <li class="phone">Fax:(888) 555-0199</li>
      <li class="email">E-Mail : dtwthecpa@ledgerpost.com</li>
      <li class="web">www : harborfilingreliefexperts.com</li>
      <li class="address">38-27, 52nd Street, sunny side, NY 11287.</li>
    </ul>

    <div class="keypad">
      <div class="key">MC</div>
      <div class="key">MR</div>
      <div class="key">MS</div>
      <div class="key">M+</div>

      <div class="key">C</div>
      <div class="key">±</div>
      <div class="key">%</div>
      <div class="key">÷</div>

      <div class="key key--digit">7</div>
      <div class="key key--digit">8</div>
      <div class="key key--digit">9</div>
      <div class="key">X</div>

      <div class="key key--digit">4</div>
      <div class="key key--digit">5</div>
      <div class="key key--digit">6</div>
      <div class="key">-</div>

      <div class="key key--digit">1</div>
      <div class="key key--digit">2</div>
      <div class="key key--digit">3</div>
      <div class="key">+</div>

      <div class="key key--blank"></div>
      <div class="key">0</div>
      <div class="key">.</div>
      <div class="key key--equals">=</div>
    </div>
  </div>
</body>
</html>
```